KVR Biz Cards

We are a property management company that manages luxury level residential estates. As such, we need a business card design that gives a high end feel. The idea at the moment is to list the services offered on the back of the card, and our company information on the front of the card.

Services for the back of the card are as follows:
Professional Property Management service, Home Hosting & Concierge Service, Holliday Home / Income Property Management

```html
<!DOCTYPE html>
<html lang="en">
<head>
<meta charset="utf-8">
<title>KVR Business Cards</title>
<link rel="stylesheet" href="https://fonts.googleapis.com/css2?family=Lato:wght@400;700&display=swap">
<style>
  :root {
    --backdrop: #d9d9d9;
    --card: #050505;
    --gold: #a97f2f;
  }
  * { box-sizing: border-box; margin: 0; padding: 0; }
  html, body {
    width: 1200px;
    height: 846px;
    overflow: hidden;
    background: var(--backdrop);
    font-family: "Lato", sans-serif;
  }
  .sheet {
    width: 1200px;
    height: 846px;
    display: flex;
    align-items: center;
    justify-content: center;
    gap: 48px;
  }
  .card {
    width: 520px;
    height: 336px;
    background: var(--card);
    color: var(--gold);
    position: relative;
    box-shadow: 0 14px 30px rgba(0, 0, 0, 0.18);
  }

  /* Front: brand name left, contact details right */
  .card-front {
    display: flex;
    align-items: center;
    justify-content: center;
    gap: 48px;
  }
  .brand-name {
    font-size: 44px;
    font-weight: 400;
    letter-spacing: 4px;
    line-height: 1;
    color: var(--gold);
  }
  .contact {
    font-size: 15px;
    line-height: 1.3;
  }
  .contact-name {
    font-weight: 700;
    font-size: 17px;
  }
  .contact-address {
    margin-top: 14px;
  }

  /* Back: brand stacked over services */
  .card-back {
    display: flex;
    flex-direction: column;
    align-items: center;
    justify-content: center;
    text-align: center;
  }
  .card-back .brand-name {
    font-size: 40px;
  }
  .company {
    margin-top: 14px;
    font-size: 20px;
    letter-spacing: 1px;
  }
  .tagline {
    font-size: 12.5px;
    letter-spacing: 0.3px;
  }
  .services {
    list-style: none;
    margin-top: 24px;
    font-size: 13.5px;
    line-height: 1.35;
  }
</style>
</head>
<body>
  <main class="sheet">
    <section class="card card-front" aria-label="Card front">
      <span class="brand-name">KVR</span>
      <div class="contact">
        <p class="contact-name">Name Surname</p>
        <p>Tel. +34-900-555-214</p>
        <p>www.kvrislands.com</p>
        <div class="contact-address">
          <p>Placa Serena Local 7,</p>
          <p>Port Celesta, 07990,</p>
          <p>Mallorca, Spain</p>
        </div>
      </div>
    </section>

    <section class="card card-back" aria-label="Card back">
      <span class="brand-name">KVR</span>
      <p class="company">KEVRAN MANAGEMENT</p>
      <p class="tagline">Crafted to Keep Every Home at Ease</p>
      <ul class="services">
        <li>Professional Property Management Service</li>
        <li>Home Hosting &amp; Concierge Service</li>
        <li>Holliday Home / Income Property Management</li>
      </ul>
    </section>
  </main>
</body>
</html>
```